40-year-old commercial construction firm :: Business Card Revamp

We are a 40 year-old, private general construction company based in Dallas, Texas, and we are considering updating our business cards, which could lead to a larger "brand refresh" campaign.

We work in a competitive environment, selling to business owners and executives making large scale purchasing decisions on behalf of their firms. A majority of our business is repeat business, with a long sales-cycle; while business can be difficult to identify and land, the effort is often rewarded with multiple projects.

We are open to a logo "refresh" as well as designs that incorporate the existing logo.

Target Market(s)

B2B selling to business owners/executives/end users who make facility decisions for their firms.

Industry/Entity Type

Construction Company

Contact Information for Business Card

Refresh from the example provided

Logo Text

Harkel Building Company :: See card example

Font styles to use
Other font styles liked:
• See sample card :: Designers to choose

Colors

Designer to choose colors to be used in the design.

Requirements
Must have
• Design should convey:
• Confidence
• Competence
• Capability
• Stability
• Tagline: Genuine Relationships :: Superior Services :: Environmentally Aware
Nice to have
• A solid design that is transferable from print to online.
• Note that we are also considering a painted-edge printing / card design
Should not have
• Too much color or whimsy. Our clients tend to be the serious type, and we work hard to present a serious, professional presence in the marketplace.

```html
<!DOCTYPE html>
<html lang="en">
<head>
<meta charset="utf-8">
<title>Harkel Building Company – Business Card</title>
<link href="https://fonts.googleapis.com/css2?family=Source+Sans+3:wght@400;600;700&display=swap" rel="stylesheet">
<style>
  :root {
    --canvas-bg: #e9e7e2;
    --card-ink: #1e1a17;
    --card-edge: #a8951f;
    --gold: #c2a72a;
    --text-light: #f2efe6;
    --text-soft: #d9d4c4;
  }
  * { box-sizing: border-box; margin: 0; padding: 0; }
  html, body {
    width: 1200px; height: 799px; overflow: hidden;
    background: var(--canvas-bg);
    font-family: "Source Sans 3", "Myriad Pro", Arial, sans-serif;
  }
  .stage {
    width: 1200px; height: 799px;
    display: flex; align-items: center; justify-content: center; gap: 60px;
  }
  .card {
    position: relative;
    width: 500px; height: 286px;
    background: var(--card-ink);
    border-bottom: 8px solid var(--card-edge);
    border-left: 4px solid var(--card-edge);
    color: var(--text-light);
    box-shadow: 0 10px 24px rgba(0,0,0,.18);
  }
  .brand { display: flex; align-items: center; gap: 10px; }
  .brand-dot {
    width: 26px; height: 26px; border-radius: 50%;
    background: var(--gold);
  }
  .brand-name {
    font-weight: 600; font-size: 34px; line-height: 1; color: var(--text-light);
    letter-spacing: -0.5px;
  }
  .brand-sub {
    font-size: 9.5px; letter-spacing: 0.6px; text-transform: uppercase;
    color: var(--text-soft); margin-top: 2px;
  }

  /* front */
  .card-front .brand { position: absolute; left: 34px; top: 60px; }
  .person { position: absolute; left: 290px; top: 58px; }
  .person-name { font-weight: 700; font-size: 19px; color: var(--gold); }
  .person-role { font-size: 12px; color: var(--text-soft); margin-bottom: 8px; }
  .contact-line {
    display: flex; align-items: center; gap: 7px;
    font-size: 12px; color: var(--text-light); line-height: 1.6;
    white-space: nowrap;
  }
  .icon { width: 11px; height: 11px; flex: none; }
  .office { position: absolute; left: 34px; bottom: 28px; }
  .office-title {
    font-size: 13px; letter-spacing: 0.4px; text-transform: uppercase;
    color: var(--text-light); margin-bottom: 4px;
  }
  .office .contact-line { gap: 6px; }
  .office .sep { display: inline-block; width: 10px; }

  /* back */
  .card-back .brand {
    position: absolute; left: 50%; top: 46%; transform: translate(-50%, -50%);
  }
  .card-back .brand-dot { width: 34px; height: 34px; }
  .card-back .brand-name { font-size: 44px; }
  .card-back .brand-sub { font-size: 11px; }
  .tagline {
    position: absolute; left: 0; right: 0; bottom: 30px;
    text-align: center; white-space: nowrap;
    font-size: 10.5px; letter-spacing: 0.8px; text-transform: uppercase;
    color: var(--gold);
  }
  .tagline .divider { margin: 0 6px; color: var(--text-soft); }
</style>
</head>
<body>
<main class="stage">

  <section class="card card-front" aria-label="Business card front">
    <div class="brand">
      <span class="brand-dot"></span>
      <div>
        <div class="brand-name">Harkel</div>
        <div class="brand-sub">Building Company, Ltd</div>
      </div>
    </div>

    <div class="person">
      <div class="person-name">Dale Porter</div>
      <div class="person-role">Business Development</div>
      <div class="contact-line">
        <svg class="icon" viewBox="0 0 12 12"><circle cx="6" cy="6" r="6" fill="var(--gold)"/><path d="M4 3.2c.4-.3.8-.2 1 .2l.5 1c.1.3 0 .5-.2.7l-.3.2c.3.8.9 1.4 1.7 1.7l.2-.3c.2-.2.4-.3.7-.2l1 .5c.4.2.5.6.2 1-.5.7-1.3.8-2.2.4C5 7.7 4.3 7 3.6 5.4c-.4-.9-.2-1.7.4-2.2z" fill="var(--card-ink)"/></svg>
        214 555 0182
      </div>
      <div class="contact-line">
        <svg class="icon" viewBox="0 0 12 12"><circle cx="6" cy="6" r="6" fill="var(--gold)"/><circle cx="6" cy="6" r="2.8" fill="none" stroke="var(--card-ink)" stroke-width="1.1"/><circle cx="6" cy="6" r="1" fill="var(--card-ink)"/></svg>
        dporter@harkelbuild.com
      </div>
    </div>

    <div class="office">
      <div class="office-title">U.S. Corporate Office</div>
      <div class="contact-line">
        <svg class="icon" viewBox="0 0 12 12"><circle cx="6" cy="6" r="6" fill="var(--gold)"/><path d="M6 2.5a2.2 2.2 0 0 1 2.2 2.2C8.2 6.3 6 9 6 9S3.8 6.3 3.8 4.7A2.2 2.2 0 0 1 6 2.5z" fill="var(--card-ink)"/><circle cx="6" cy="4.7" r=".8" fill="var(--gold)"/></svg>
        1180 Marlow Street, Dallas, Texas 75201
      </div>
      <div class="contact-line">
        <svg class="icon" viewBox="0 0 12 12"><circle cx="6" cy="6" r="6" fill="var(--gold)"/><path d="M4 3.2c.4-.3.8-.2 1 .2l.5 1c.1.3 0 .5-.2.7l-.3.2c.3.8.9 1.4 1.7 1.7l.2-.3c.2-.2.4-.3.7-.2l1 .5c.4.2.5.6.2 1-.5.7-1.3.8-2.2.4C5 7.7 4.3 7 3.6 5.4c-.4-.9-.2-1.7.4-2.2z" fill="var(--card-ink)"/></svg>
        972 555 0143
        <span class="sep"></span>
        <svg class="icon" viewBox="0 0 12 12"><circle cx="6" cy="6" r="6" fill="var(--gold)"/><rect x="3" y="4" width="6" height="4.5" rx=".6" fill="var(--card-ink)"/><rect x="4" y="2.6" width="4" height="1.6" fill="var(--card-ink)"/></svg>
        972 555 0171
        <span class="sep"></span>
        <svg class="icon" viewBox="0 0 12 12"><circle cx="6" cy="6" r="6" fill="var(--gold)"/><circle cx="6" cy="6" r="3.2" fill="none" stroke="var(--card-ink)" stroke-width=".9"/><path d="M2.8 6h6.4M6 2.8c-1.4 1.8-1.4 4.6 0 6.4M6 2.8c1.4 1.8 1.4 4.6 0 6.4" fill="none" stroke="var(--card-ink)" stroke-width=".8"/></svg>
        harkelbuild.com
      </div>
    </div>
  </section>

  <section class="card card-back" aria-label="Business card back">
    <div class="brand">
      <span class="brand-dot"></span>
      <div>
        <div class="brand-name">Harkel</div>
        <div class="brand-sub">Building Company, Ltd</div>
      </div>
    </div>
    <p class="tagline">Genuine Relationships<span class="divider">::</span>Superior Services<span class="divider">::</span>Environmentally Aware</p>
  </section>

</main>
</body>
</html>
```